Banner to celebrate Pellway Journeys 40 years in business. Will be used on our social media channels.

Hello
We would like a banner created to celebrate 40 years in business with tagline "service through experience since 1983"
also add our website pellwayjourneys.com.au
Banner size must be : 650 x 150px
open to suggestions

Target Market(s)

current and prospective clients

Industry/Entity Type

Travel & Tourism (Business Travel)

Colors
0054AA
0677BA
7BADD7
CADEEF
E8F1F8

Requirements
Must have
• use current theme of our website www.pellwayjourneys.com.au. Keep simple and effective.
Nice to have
• use one image that I have provided
Should not have
• multiple graphics

```html
<!DOCTYPE html>
<html lang="en">
<head>
<meta charset="utf-8">
<title>Pellway Journeys – 40 Years in Business</title>
<link rel="stylesheet" href="https://fonts.googleapis.com/css2?family=Great+Vibes&family=Rubik:wght@500;700&family=Roboto:wght@400;500;700&display=swap">
<style>
  :root {
    --page-bg: #ececec;
    --navy: #0b1a3c;
    --gold: #a97944;
    --white: #ffffff;
    --sky-top: #bfe6f2;
    --sea: #4aa7bd;
    --sea-deep: #2f7f98;
    --shore: #c9a46a;
  }
  html, body {
    margin: 0;
    padding: 0;
    width: 1200px;
    height: 1159px;
    overflow: hidden;
    background: var(--page-bg);
  }
  .banner {
    position: absolute;
    left: 80px;
    top: 459px;
    width: 1040px;
    height: 240px;
    overflow: hidden;
  }
  .banner-photo {
    position: absolute;
    inset: 0;
    background:
      linear-gradient(180deg, transparent 72%, rgba(201,164,106,0.85) 98%),
      linear-gradient(100deg, rgba(255,255,255,0.4) 0%, transparent 45%),
      linear-gradient(180deg, var(--sky-top) 0%, #d8eef2 28%, #6fa28a 44%, var(--sea) 56%, var(--sea-deep) 82%);
  }
  .banner-copy {
    position: absolute;
    left: 110px;
    top: 30px;
    color: var(--navy);
  }
  .headline-script {
    display: block;
    margin-left: 40px;
    font-family: "Great Vibes", cursive;
    font-size: 54px;
    line-height: 52px;
  }
  .headline-main {
    display: block;
    margin-top: 2px;
    font-family: "Rubik", sans-serif;
    font-weight: 700;
    font-size: 30px;
    line-height: 36px;
    letter-spacing: -0.3px;
    white-space: nowrap;
  }
  .headline-main .light { font-weight: 500; }
  .tagline {
    display: inline-flex;
    margin-top: 8px;
    border: 1px solid var(--navy);
    height: 26px;
    font-family: "Roboto", sans-serif;
    font-size: 16px;
    line-height: 26px;
    white-space: nowrap;
  }
  .tagline-text { padding: 0 8px 0 9px; }
  .tagline-year {
    padding: 0 6px;
    background: var(--gold);
    color: var(--white);
    font-weight: 700;
  }
  .website {
    display: block;
    margin-top: 10px;
    font-family: "Roboto", sans-serif;
    font-weight: 500;
    font-size: 15px;
    line-height: 18px;
    letter-spacing: 0.4px;
  }
</style>
</head>
<body>
  <section class="banner">
    <div class="banner-photo" role="img" aria-label="Traveller with hat and backpack standing on rocks overlooking a blue lake and green mountains"></div>
    <div class="banner-copy">
      <span class="headline-script">Celebrate</span>
      <span class="headline-main">40 years <span class="light">in</span> Business</span>
      <div class="tagline">
        <span class="tagline-text">Service Through Experience</span>
        <span class="tagline-year">Since 1983</span>
      </div>
      <span class="website">pellwayjourneys.com.au</span>
    </div>
  </section>
</body>
</html>
```